VALMIRA/ VALMIRA GREY Business Card

We have two brands that we would like to show one 1 business card (front and back). We would to incorporate two different logos on one card (VALMIRA and VALMIRA GREY). Card can be two sided. Simple, sleek and professional.

We are a senior living provider.

www.valmira-example.com
www.valmiragrey-example.com

Target Market(s)

Professionals

Industry/Entity Type

Business

Font styles to use
Serif

Colors

Designer to choose colors to be used in the design.

Requirements
Must have
• Space for EMAIL, PHONE, WEBSITE
Nice to have
• Raised lettering or gloss lettering

```html
<!DOCTYPE html>
<html lang="en">
<head>
<meta charset="utf-8">
<title>VALMIRA / VALMIRA GREY Business Card</title>
<link rel="stylesheet" href="https://fonts.googleapis.com/css2?family=Cinzel:wght@400&family=PT+Sans:wght@400&display=swap">
<style>
  :root {
    --page: #ffffff;
    --card: #2b2a29;
    --card-deep: #1e1d1b;
    --gold: #c1952f;
    --gold-line: #a8842f;
    --ink-light: #ffffff;
    --serif: "Cinzel", "Times New Roman", serif;
    --sans: "PT Sans", "Helvetica Neue", Arial, sans-serif;
  }
  * { box-sizing: border-box; margin: 0; padding: 0; }
  html, body {
    width: 1200px; height: 1200px; overflow: hidden;
    background: var(--page);
  }
  .sheet { position: relative; width: 1200px; height: 1200px; }

  .card {
    position: absolute;
    left: 260px;
    width: 686px;
    height: 428px;
    border-radius: 9px;
    background: var(--card);
    overflow: hidden;
  }
  .card--front { top: 139px; }
  .card--back  { top: 649px; }

  /* front brand */
  .front-brand {
    position: absolute;
    left: 0; right: 0; top: 150px;
    display: flex; align-items: center; justify-content: center;
    gap: 26px;
  }
  .front-brand__square {
    width: 92px; height: 92px;
    background: var(--gold);
  }
  .front-brand__name {
    font-family: var(--serif);
    font-weight: 400;
    font-size: 86px;
    line-height: 1;
    letter-spacing: 2px;
    color: var(--gold);
  }

  /* back bands */
  .back-band {
    position: absolute;
    left: 0; right: 0;
    top: 85px; height: 258px;
    background: var(--card-deep);
  }
  .back-brand {
    position: absolute;
    left: 41px; top: 170px;
  }
  .back-brand__name {
    font-family: var(--serif);
    font-weight: 400;
    font-size: 54px;
    line-height: 1;
    letter-spacing: 1px;
    color: var(--ink-light);
    white-space: nowrap;
  }
  .back-brand__tagline {
    margin-top: 10px;
    font-family: var(--sans);
    font-size: 28px;
    line-height: 1;
    color: var(--ink-light);
    white-space: nowrap;
  }

  /* contact strip */
  .contact-rule {
    position: absolute;
    left: 41px; right: 41px;
    height: 2px;
    background: var(--gold-line);
  }
  .card--front .contact-rule { top: 372px; }
  .card--back  .contact-rule { top: 370px; }

  .contact-list {
    position: absolute;
    left: 41px; right: 41px;
    display: flex; justify-content: space-between;
    list-style: none;
    font-family: var(--sans);
    font-size: 16px;
    line-height: 1;
    color: var(--ink-light);
  }
  .card--front .contact-list { top: 380px; }
  .card--back  .contact-list { top: 379px; }
</style>
</head>
<body>
<main class="sheet">

  <section class="card card--front" aria-label="Card front">
    <div class="front-brand">
      <span class="front-brand__square" aria-hidden="true"></span>
      <span class="front-brand__name">VALMIRA</span>
    </div>
    <div class="contact-rule"></div>
    <ul class="contact-list">
      <li>www.valmira-example.com</li>
      <li>info@valmira-example.com</li>
      <li>011 555 0142</li>
    </ul>
  </section>

  <section class="card card--back" aria-label="Card back">
    <div class="back-band"></div>
    <div class="back-brand">
      <div class="back-brand__name">VALMIRA GREY</div>
      <div class="back-brand__tagline">Executive Personal Care Services</div>
    </div>
    <div class="contact-rule"></div>
    <ul class="contact-list">
      <li>www.valmiragrey-example.com</li>
      <li>info@valmiragrey-example.com</li>
      <li>011 555 0176</li>
    </ul>
  </section>

</main>
</body>
</html>
```